Flyer-Design für Immobilienmarketing von Raumfreude Home Staging
Zielgruppe
Wir (Raumfreude Home Staging) geben mit Home Staging Immobilien ein Raumfreude (www.raumfreude-beispiel.de). Ziel ist die Immobilienvermarktung zu beschleunigen (Immobilienmarketing) und den besten Preis zu erzielen. Durch ein eigenes Möbel und Dekolager erfolgt die Gestaltung zeitnah.
Zielgruppe sind Immobilienverkäufer (privat) und auch Makler/Vermittler/Projektentwickler
Aufgabenstellung
Wir benötigen einen Flyer/Klappkarte DIN lang quer. Dieser sollte hochwertig, einladend, hell und freundlich erscheinen. Wenn er an der langen Seite gefaltet ist, sollte er als Klappkarte auf dem Tisch stehen können. Dabei sollen alle 4 Seiten genutzt werden. Logo und Design sowie Kurzbeschreibungen/Texte entsprechend bitte der Website (www.raumfreude-beispiel.de) verwenden. Originale können zur Verfügung gestellt werden. Der Flyer sollte auch als PDF nutzbar sein.
Als Slogan stellen wir uns folgendes vor 'Mit Raumfreude in den Immobilienverkauf starten und beim besten Preis landen', sind aber für alles offen. Bei Verwendung von Referenzen wäre ein Spruch mit 'Wohlfühlen' gut. Des Weiteren einfach bei den Texten und Bildern der Website bedienen (Vorteile + warum mit uns) und einen knackigen überzeugenden Flyer bei dem hauptsächlich die Bilder sprechen, erstellen. Wir freuen uns auf die Vorschläge.

```html
<!DOCTYPE html>
<html lang="de">
<head>
<meta charset="utf-8">
<title>Raumfreude Home Staging – Klappkarte</title>
<link href="https://fonts.googleapis.com/css2?family=Ubuntu:wght@300;400;500;700&display=swap" rel="stylesheet">
<style>
  :root {
    --backdrop: #3a3a3a;
    --paper: #f4f4f4;
    --paper-white: #f7f7f7;
    --green: #8cc43c;
    --ink: #3c3c3c;
    --ink-soft: #555555;
    --photo-light: #e9e4dc;
    --photo-mid: #cfc6b8;
    --photo-wood: #b48d62;
    --photo-green: #5f8a55;
  }
  * { box-sizing: border-box; margin: 0; padding: 0; }
  html, body {
    width: 1200px; height: 960px; overflow: hidden;
    background: var(--backdrop);
    font-family: "Ubuntu", sans-serif;
    color: var(--ink);
  }
  .sheet {
    position: absolute; left: 150px; width: 900px; height: 425px;
    background: var(--paper);
    box-shadow: 0 10px 30px rgba(0,0,0,.35);
    overflow: hidden;
  }
  .sheet--cover { top: 40px; }
  .sheet--inside { top: 495px; }

  /* Cover */
  .cover-photo {
    position: absolute; left: 0; top: 0; width: 380px; height: 100%;
    background: linear-gradient(135deg, var(--photo-light) 0%, #f3f0ea 40%, var(--photo-mid) 70%, var(--photo-wood) 100%);
  }
  .cover-photo::after {
    content: ""; position: absolute; right: 60px; bottom: 80px; width: 90px; height: 90px;
    border-radius: 50%; background: var(--photo-green); opacity: .55; filter: blur(18px);
  }
  .cover-content {
    position: absolute; left: 380px; right: 0; top: 0; bottom: 0;
    background: var(--paper-white);
    padding: 70px 60px 0 70px;
  }
  .slogan {
    font-weight: 300; font-size: 25px; line-height: 1.3; color: var(--ink-soft);
  }
  .slogan-rule { width: 330px; height: 2px; background: var(--green); margin: 30px 0 26px; }
  .brand-name {
    font-weight: 300; font-size: 62px; line-height: 1; color: var(--ink); letter-spacing: -.5px;
  }
  .brand-tagline {
    margin-top: 10px; font-weight: 300; font-size: 18px; letter-spacing: 6px; color: var(--ink-soft);
  }
  .brand-url { margin-top: 22px; font-size: 15px; color: var(--ink-soft); }

  /* Inside */
  .inside-photo {
    position: absolute; left: 0; top: 0; width: 100%; height: 300px;
    background: linear-gradient(100deg, #8d6f52 0%, var(--photo-light) 22%, #f5f2ec 50%, var(--photo-mid) 75%, #e7e1d6 100%);
  }
  .inside-photo::after {
    content: ""; position: absolute; left: 420px; top: 150px; width: 300px; height: 110px;
    border-radius: 30px; background: #eeeae3; opacity: .8; filter: blur(8px);
  }
  .headline-band {
    position: absolute; left: 70px; top: 40px; width: 330px; height: 160px;
    background: var(--green); color: #fff;
    display: flex; align-items: center; padding: 0 30px;
    font-weight: 500; font-size: 27px; line-height: 1.3;
  }
  .benefits {
    position: absolute; left: 0; right: 0; bottom: 0; height: 125px;
    display: flex; align-items: center; padding: 0 50px;
    background: var(--paper-white);
  }
  .benefit { flex: 1; }
  .benefit h2 { font-weight: 700; font-size: 17px; color: var(--ink); margin-bottom: 8px; }
  .benefit p { font-weight: 400; font-size: 14px; line-height: 1.45; color: var(--ink-soft); }
  .benefit-divider { width: 2px; height: 70px; background: var(--green); margin: 0 40px; }
</style>
</head>
<body>

<section class="sheet sheet--cover">
  <div class="cover-photo" role="img" aria-label="Foto eines hellen, eingerichteten Wohnraums mit Fenstern, grünem Sessel und Holzboden"></div>
  <div class="cover-content">
    <p class="slogan">Mit Raumfreude in den<br>Immobilienverkauf starten<br>und beim besten Preis landen</p>
    <div class="slogan-rule"></div>
    <p class="brand-name">raumfreude</p>
    <p class="brand-tagline">HOME STAGING</p>
    <p class="brand-url">www.raumfreude-beispiel.de</p>
  </div>
</section>

<section class="sheet sheet--inside">
  <div class="inside-photo" role="img" aria-label="Foto eines gestalteten Wohnzimmers mit hellem Sofa, Kissen, Pflanzen und Teppich"></div>
  <h1 class="headline-band">Wir geben Räumen<br>ein Gesicht zum Wohlfühlen</h1>
  <div class="benefits">
    <div class="benefit">
      <h2>Schnelle &amp; individuelle Einrichtung</h2>
      <p>Mit unserem eigenen Möbellager garantieren Wir Ihnen eine schnelle und individuelle Einrichtung Ihrer Immobilie</p>
    </div>
    <div class="benefit-divider"></div>
    <div class="benefit">
      <h2>Wir wissen was gut ankommt!</h2>
      <p>Unsere gesammelten Erfahrungen setzen wir gezielt ein, damit sich jede Immobilie schnell und zum besten Preis verkauft.</p>
    </div>
  </div>
</section>

</body>
</html>
```